Modern labels for Tidlock products

We need a new design of our labels for the product “Tidlock” (https://www.tidlock.eu/#) . The reason why we want to change our labels is to get a modern and more advanced look of our product. We also want to create a unique product that is attractive for our customers, even if the product are used in hospitals and healthcare centers for collecting dangerous waste.

There is three sizes of labels (55x95, 90x95, 170x95 mm) for different boxes, but the label will contain similar information. There are certain requirements and factors from regulations/standards that you need to follow when you create the new layout. But it’s up to you to change the design. You can work with background, fonts, effects, colors, structure, pattern, new symbols, logotype etc. The label could be any color, but the container will stay yellow so they have to look good together.

Keywords: Elegant, modern, functional, attractive, exclusive

Target Market(s)

Hospitals and healthcare centers

Industry/Entity Type

Product

Font styles to use
Serif
Sans Serif

Colors

Designer to choose colors to be used in the design.

Requirements
Must have
• Requirements for the regulations ADR UN3291 and ISO 23907 (PDF).
• * Symbol for danger waste
• * Filling level
• * "Danger"
• * Symbol for no second use
• * Symbol for manufaturer
• * Referencenumber
• * Text "”Clinical waste, Unspecified, N.O.S.”"
• * Area for series, certification, size and useful capacity
• * Area for Illustrations.
• * Text “Autoclavable at 134 c”, “Do not force closure” and “Do not overfill”.
• * Text for certification ”UN 3291 1H2/Y0,3/S/YR/N/KVP4817B”
• Three different sizes (55x95, 90x95, 170x95).
• More info in PDF "3kravspecifikation"
Nice to have
• A modern, elegant, advanced look of our label.
Should not have
• The information must be clear and readable, not too decorative/handwriting fonts.

```html
<!DOCTYPE html>
<html lang="en">
<head>
<meta charset="utf-8">
<title>Tidlock clinical waste labels</title>
<link href="https://fonts.googleapis.com/css2?family=Oswald:wght@500;700&family=Roboto+Condensed:ital,wght@0,400;0,700;1,700&family=Roboto:wght@700;900&family=Roboto+Slab:wght@800&display=swap" rel="stylesheet">
<style>
  :root {
    --label-yellow: #fbe11f;
    --warning-red: #e8231d;
    --ink: #111111;
    --paper: #ffffff;
    --panel-grey: #e9e9e9;
    --hazard-grey: #2a2a2a;
    --maker-red: #a3120e;
  }
  html, body { margin: 0; width: 1042px; height: 1200px; overflow: hidden; background: var(--paper); }
  .sheet { display: block; width: 1042px; height: 1200px; }
  .label-base { fill: var(--label-yellow); }
  .red-field { fill: var(--warning-red); }
  .diamond-outer { fill: var(--paper); }
  .diamond-inner { fill: var(--paper); stroke: var(--ink); stroke-width: 3; }
  .hazard-symbol { fill: var(--hazard-grey); }
  .instruction-panel { fill: var(--panel-grey); stroke: var(--ink); stroke-width: 3; }
  .info-box { fill: var(--paper); stroke: var(--ink); stroke-width: 2; }
  .rule { stroke: var(--ink); }
  .level-arrow { fill: var(--ink); }
  .level-text { fill: var(--label-yellow); font-family: "Roboto", Arial, sans-serif; font-weight: 900; }
  .waste-title { fill: var(--paper); font-family: "Oswald", "Arial Narrow", sans-serif; font-weight: 700; }
  .danger-word { fill: var(--warning-red); font-family: "Oswald", "Arial Narrow", sans-serif; font-weight: 700; text-anchor: middle; }
  .substance-word { fill: var(--ink); font-family: "Roboto Slab", Georgia, serif; font-weight: 800; text-anchor: middle; }
  .notice-line { fill: var(--ink); font-family: "Roboto Condensed", "Arial Narrow", sans-serif; text-anchor: middle; }
  .class-number { fill: var(--ink); font-family: "Oswald", "Arial Narrow", sans-serif; font-weight: 700; text-anchor: middle; }
  .un-number { font-family: "Roboto", Arial, sans-serif; font-weight: 900; }
  .un-code { font-family: "Roboto Condensed", "Arial Narrow", sans-serif; }
  .brand-name { font-family: "Roboto", Arial, sans-serif; font-weight: 700; }
  .small-print { fill: var(--ink); font-family: "Roboto Condensed", "Arial Narrow", sans-serif; }
  .small-print .strong { font-weight: 700; font-style: italic; }
  .maker-address { fill: var(--maker-red); font-family: "Roboto Condensed", "Arial Narrow", sans-serif; }
  .reuse-ring { fill: none; }
  .reuse-ring.dark { stroke: var(--ink); }
  .reuse-ring.light { stroke: var(--paper); }
  .reuse-digit { font-family: "Roboto", Arial, sans-serif; font-weight: 700; text-anchor: middle; }
  .white { fill: var(--paper); }
  .black { fill: var(--ink); }
</style>
</head>
<body>
<svg class="sheet" viewBox="0 0 1300 1500" xmlns="http://www.w3.org/2000/svg">
  <defs>
    <symbol id="manufacturer" viewBox="0 0 54 38">
      <path d="M0 38V14l12 8v-8l12 8v-8l12 8V0h9v38z" fill="#111"/>
    </symbol>
  </defs>

  <!-- Wide label 170x95 -->
  <g class="label-wide">
    <rect class="label-base" x="67" y="70" width="1168" height="652" rx="30"/>
    <path class="red-field" d="M140 112H912L636 398L912 688H140Q110 688 110 658V142Q110 112 140 112Z"/>

    <polygon class="level-arrow" points="148,150 196,126 196,133 717,133 717,126 765,150 717,174 717,167 196,167 196,174"/>
    <text class="level-text" x="295" y="161" font-size="29" textLength="325">FILLING LEVEL</text>
    <text class="waste-title" x="150" y="218" font-size="47" textLength="620" lengthAdjust="spacingAndGlyphs">Clinical Waste, Unspecified, N.O.S.</text>

    <rect class="instruction-panel" x="151" y="241" width="350" height="258" role="img" aria-label="Step-by-step illustrations for opening, closing and filling the container"/>

    <text class="un-number white" font-size="64" transform="translate(568 492) rotate(-90)" textLength="245" lengthAdjust="spacingAndGlyphs">UN3291</text>
    <g transform="translate(596 492) rotate(-90)">
      <circle cx="10" cy="-7" r="10" fill="none" stroke="#fff" stroke-width="1.6"/>
      <text class="un-code white" x="10" y="-3" font-size="10" text-anchor="middle">un</text>
      <text class="un-code white" x="25" y="0" font-size="21" textLength="220" lengthAdjust="spacingAndGlyphs">1H2/Y0.7/S/YR/N/KVP4817B</text>
    </g>

    <rect class="info-box" x="150" y="515" width="502" height="58" rx="4"/>
    <text class="small-print" x="172" y="537" font-size="16">Autoclavable at 134 C</text>
    <text class="small-print" x="326" y="537" font-size="16">•</text>
    <text class="small-print" x="346" y="537" font-size="16">Do not force closure</text>
    <text class="small-print" x="509" y="537" font-size="16">•</text>
    <text class="small-print" x="545" y="537" font-size="16">Do not overfill</text>
    <text class="small-print" x="157" y="563" font-size="16" textLength="487" lengthAdjust="spacingAndGlyphs">Series: <tspan class="strong" font-size="19">Aria</tspan> Certification: <tspan class="strong">ISO 23907:2012</tspan>  Size: <tspan class="strong">2,2 L</tspan>  Usefulcapcity: 1,76 L</text>

    <use href="#manufacturer" x="150" y="613" width="54" height="38"/>
    <rect x="218" y="600" width="12" height="12" class="white"/>
    <text class="brand-name white" x="236" y="618" font-size="26">Tidlock</text>
    <text class="maker-address" x="218" y="636" font-size="11">Lundvik, Sweden</text>
    <text class="maker-address" x="218" y="650" font-size="11">www.tidlock.eu</text>

    <rect class="info-box" x="377" y="587" width="276" height="75"/>
    <line class="rule" x1="377" y1="612" x2="653" y2="612" stroke-width="2"/>
    <line class="rule" x1="377" y1="637" x2="653" y2="637" stroke-width="2"/>
    <text class="small-print" x="384" y="603" font-size="12">Etablissement</text>
    <text class="small-print" x="384" y="629" font-size="12">Unité de soins</text>
    <text class="small-print" x="384" y="654" font-size="12">Mise en service</text>

    <polygon class="diamond-outer" points="912,112 1192,398 912,688 636,398"/>
    <polygon class="diamond-inner" points="912,142 1164,398 912,658 662,398"/>
    <circle class="hazard-symbol" cx="914" cy="298" r="85" role="img" aria-label="Biohazard symbol"/>
    <text class="danger-word" x="914" y="441" font-size="60">DANGER</text>
    <text class="substance-word" x="914" y="477" font-size="29" textLength="306" lengthAdjust="spacingAndGlyphs">INFECTIONS SUBSTANCE</text>
    <text class="notice-line" x="914" y="507" font-size="20">In Case Of Damage Or Leakage</text>
    <text class="notice-line" x="914" y="533" font-size="20">Immediately Notify Public</text>
    <text class="notice-line" x="914" y="559" font-size="20">Health Authority</text>
    <text class="class-number" x="914" y="622" font-size="60">6</text>

    <rect x="962" y="118" width="22" height="22" class="black"/>
    <text class="brand-name black" x="996" y="150" font-size="46">Tidlock</text>

    <circle class="reuse-ring dark" cx="1117" cy="609" r="45" stroke-width="4"/>
    <text class="reuse-digit black" x="1117" y="631" font-size="62">2</text>
    <line class="rule" x1="1086" y1="640" x2="1148" y2="578" stroke-width="4"/>
  </g>

  <!-- Narrow label 55x95 -->
  <g class="label-narrow">
    <rect class="label-base" x="128" y="775" width="377" height="655" rx="22"/>
    <path class="red-field" d="M143 958H480Q490 958 490 968V1430H143Z"/>

    <polygon class="level-arrow" points="143,803 172,789 172,794 463,794 463,789 492,803 463,817 463,812 172,812 172,817"/>
    <text class="level-text" x="225" y="810" font-size="17" textLength="185">FILLING LEVEL</text>

    <rect x="145" y="832" width="12" height="12" class="black"/>
    <text class="brand-name black" x="162" y="853" font-size="26">Tidlock</text>
    <text class="un-number black" x="492" y="848" font-size="30" text-anchor="end">UN3291</text>
    <circle cx="384" cy="856" r="5" fill="none" stroke="#111" stroke-width="1"/>
    <text class="un-code black" x="492" y="860" font-size="11" text-anchor="end" textLength="100" lengthAdjust="spacingAndGlyphs">1H2/Y0.7/S/YR/N/KVP4817B</text>

    <polygon class="diamond-outer" points="318,838 440,958 318,1082 196,958"/>
    <polygon class="diamond-inner" points="318,852 425,958 318,1066 211,958" stroke-width="2"/>
    <circle class="hazard-symbol" cx="318" cy="911" r="39" role="img" aria-label="Biohazard symbol"/>
    <text class="danger-word" x="318" y="975" font-size="27">DANGER</text>
    <text class="substance-word" x="318" y="992" font-size="13" textLength="128" lengthAdjust="spacingAndGlyphs">INFECTIONS SUBSTANCE</text>
    <text class="notice-line" x="318" y="1004" font-size="8.5" textLength="104" lengthAdjust="spacingAndGlyphs">In Case Of Damage Or Leakage</text>
    <text class="notice-line" x="318" y="1015" font-size="8.5" textLength="86" lengthAdjust="spacingAndGlyphs">Immediately Notify Public</text>
    <text class="notice-line" x="318" y="1026" font-size="8.5" textLength="56" lengthAdjust="spacingAndGlyphs">Health Authority</text>
    <text class="class-number" x="318" y="1052" font-size="26">6</text>

    <circle class="reuse-ring light" cx="423" cy="1055" r="36" stroke-width="3"/>
    <text class="reuse-digit white" x="423" y="1073" font-size="50">2</text>
    <line x1="398" y1="1080" x2="448" y2="1030" stroke="#fff" stroke-width="3"/>

    <text class="waste-title" font-size="33" transform="translate(181 1420) rotate(-90)" textLength="448" lengthAdjust="spacingAndGlyphs">Clinical Waste, Unspecified, N.O.S.</text>

    <rect class="instruction-panel" x="197" y="1119" width="274" height="203" role="img" aria-label="Step-by-step illustrations for opening, closing and filling the container"/>

    <rect class="info-box" x="196" y="1337" width="276" height="33" rx="3"/>
    <text class="small-print" x="206" y="1350" font-size="9" textLength="256" lengthAdjust="spacingAndGlyphs">Autoclavable at 134 C  •  Do not force closure  •  Do not overfill</text>
    <text class="small-print" x="201" y="1364" font-size="9" textLength="266" lengthAdjust="spacingAndGlyphs">Series: <tspan class="strong">Aria</tspan> Certification: <tspan class="strong">ISO 23907:2012</tspan>  Size: <tspan class="strong">2,2 L</tspan>  Usefulcapcity: 1,76 L</text>

    <use href="#manufacturer" x="196" y="1385" width="36" height="28"/>
    <rect x="238" y="1380" width="7" height="7" class="white"/>
    <text class="brand-name white" x="248" y="1393" font-size="16">Tidlock</text>
    <text class="maker-address" x="238" y="1403" font-size="7">Lundvik, Sweden</text>
    <text class="maker-address" x="238" y="1411" font-size="7">www.tidlock.eu</text>

    <rect class="info-box" x="328" y="1377" width="144" height="39" stroke-width="1.5"/>
    <line class="rule" x1="328" y1="1390" x2="472" y2="1390" stroke-width="1.5"/>
    <line class="rule" x1="328" y1="1403" x2="472" y2="1403" stroke-width="1.5"/>
    <text class="small-print" x="333" y="1387" font-size="7">Etablissement</text>
    <text class="small-print" x="333" y="1400" font-size="7">Unité de soins</text>
    <text class="small-print" x="333" y="1413" font-size="7">Mise en service</text>
  </g>

  <!-- Square label 90x95 -->
  <g class="label-square">
    <rect class="label-base" x="556" y="777" width="617" height="653" rx="30"/>
    <path class="red-field" d="M594 1025H1136Q1148 1025 1148 1037V1430H582V1037Q582 1025 594 1025Z"/>

    <polygon class="level-arrow" points="582,816 620,797 620,802 1110,802 1110,797 1148,816 1110,835 1110,830 620,830 620,835"/>
    <text class="level-text" x="715" y="826" font-size="25" textLength="300">FILLING LEVEL</text>

    <rect x="582" y="856" width="18" height="18" class="black"/>
    <text class="brand-name black" x="610" y="886" font-size="40">Tidlock</text>
    <text class="un-number black" x="1150" y="888" font-size="46" text-anchor="end">UN3291</text>
    <circle cx="969" cy="904" r="8" fill="none" stroke="#111" stroke-width="1.3"/>
    <text class="un-code black" x="1148" y="910" font-size="15" text-anchor="end" textLength="166" lengthAdjust="spacingAndGlyphs">1H2/Y0.7/S/YR/N/KVP4817B</text>

    <polygon class="diamond-outer" points="865,855 1035,1024 865,1194 695,1024"/>
    <polygon class="diamond-inner" points="865,875 1014,1024 865,1174 716,1024" stroke-width="2.5"/>
    <circle class="hazard-symbol" cx="865" cy="950" r="55" role="img" aria-label="Biohazard symbol"/>
    <text class="danger-word" x="865" y="1052" font-size="39">DANGER</text>
    <text class="substance-word" x="865" y="1074" font-size="18" textLength="186" lengthAdjust="spacingAndGlyphs">INFECTIONS SUBSTANCE</text>
    <text class="notice-line" x="865" y="1093" font-size="12" textLength="140" lengthAdjust="spacingAndGlyphs">In Case Of Damage Or Leakage</text>
    <text class="notice-line" x="865" y="1109" font-size="12" textLength="112" lengthAdjust="spacingAndGlyphs">Immediately Notify Public</text>
    <text class="notice-line" x="865" y="1125" font-size="12" textLength="76" lengthAdjust="spacingAndGlyphs">Health Authority</text>
    <text class="class-number" x="865" y="1162" font-size="38">6</text>

    <circle class="reuse-ring light" cx="1053" cy="1140" r="46" stroke-width="4"/>
    <text class="reuse-digit white" x="1053" y="1163" font-size="64">2</text>
    <line x1="1021" y1="1172" x2="1085" y2="1108" stroke="#fff" stroke-width="4"/>

    <text class="waste-title" x="605" y="1158" font-size="36" textLength="176" lengthAdjust="spacingAndGlyphs">Clinical Waste,</text>
    <text class="waste-title" x="605" y="1206" font-size="36" textLength="222" lengthAdjust="spacingAndGlyphs">Unspecified, N.O.S.</text>

    <rect class="instruction-panel" x="601" y="1227" width="255" height="188" role="img" aria-label="Step-by-step illustrations for opening, closing and filling the container"/>

    <rect class="info-box" x="876" y="1228" width="258" height="45" rx="3"/>
    <text class="small-print" x="888" y="1244" font-size="9" textLength="234" lengthAdjust="spacingAndGlyphs">Autoclavable at 134 C   •   Do not force closure   •   Do not overfill</text>
    <text class="small-print" x="882" y="1264" font-size="9" textLength="246" lengthAdjust="spacingAndGlyphs">Series: <tspan class="strong">Aria</tspan> Certification: <tspan class="strong">ISO 23907:2012</tspan>  Size: <tspan class="strong">2,2 L</tspan>  Usefulcapcity: 1,76 L</text>

    <rect class="info-box" x="876" y="1284" width="254" height="72" stroke-width="1.5"/>
    <line class="rule" x1="876" y1="1308" x2="1130" y2="1308" stroke-width="1.5"/>
    <line class="rule" x1="876" y1="1332" x2="1130" y2="1332" stroke-width="1.5"/>
    <text class="small-print" x="881" y="1301" font-size="11">Etablissement</text>
    <text class="small-print" x="881" y="1325" font-size="11">Unité de soins</text>
    <text class="small-print" x="881" y="1349" font-size="11">Mise en service</text>

    <use href="#manufacturer" x="880" y="1378" width="36" height="28"/>
    <rect x="922" y="1374" width="8" height="8" class="white"/>
    <text class="brand-name white" x="933" y="1387" font-size="16">Tidlock</text>
    <text class="maker-address" x="922" y="1397" font-size="7.5">Lundvik, Sweden</text>
    <text class="maker-address" x="922" y="1406" font-size="7.5">www.tidlock.eu</text>
  </g>
</svg>
</body>
</html>
```